Company or website name
- www.tovirka.me
- Describe your company and organization and target audience
- Our small factory makes organic chocolate with honey instead of sugar and creates jobs for people with special needs in Pereslavl-Zalessky / Russia.
- The design should have the following
- At the moment we are searching for a designer to create some labels for new tastes of chocolate in the same style we already use. Here are some examples of our packagings: http://tovirka.me/product-category/assortment/ What we need are illustrations of new tastes in the center of the packaging. The rest of the packaging should remain unchanged. The new tastes are: - Dark chocolate with Goji berries and crushed cocoa beans - Dark chocolate with Cashew nuts and basil - Dark chocolate with Hibisсus - Dark chocolate with Barberry - Milk chocolate We can pay 100 $ for the five labels (20 $ for each). We know, it's not a lot, but we hope to find the right

```html
<!DOCTYPE html>
<html lang="ru">
<head>
<meta charset="utf-8">
<title>Шоколад на меду — этикетки</title>
<link rel="stylesheet" href="https://fonts.googleapis.com/css2?family=Montserrat:wght@600&family=Oswald:wght@400;500&family=PT+Sans+Narrow&family=Marck+Script&display=swap">
<style>
  :root {
    --page: #f4f1ec;
    --kraft: #d7bb8f;
    --kraft-dark: #c9a979;
    --ink: #2b2621;
    --ink-soft: #4a4038;
    --green: #4f7a35;
    --ribbon: #2a2520;
    --ribbon-text: #e8dcc4;
    --nut: #7a5a45;
    --leaf: #4f7a35;
    --berry: #9a2f25;
    --bean: #5a3b2c;
  }
  * { box-sizing: border-box; margin: 0; padding: 0; }
  html, body { width: 1200px; height: 959px; overflow: hidden; }
  body {
    background: var(--page);
    display: flex;
    align-items: center;
    justify-content: center;
    gap: 70px;
  }
  .label {
    width: 400px;
    height: 780px;
    background: var(--kraft);
    background-image: radial-gradient(circle at 30% 20%, #dcc197 0%, var(--kraft) 55%, var(--kraft-dark) 100%);
    box-shadow: 0 10px 30px rgba(60, 40, 20, .18);
    display: flex;
    flex-direction: column;
    align-items: center;
    padding-top: 46px;
    color: var(--ink);
    position: relative;
  }
  .brand-mark {
    width: 58px; height: 58px;
    border: 2px solid var(--ink-soft);
    border-radius: 50%;
  }
  .brand-name {
    margin-top: 16px;
    font-family: "PT Sans Narrow", sans-serif;
    font-size: 22px;
    line-height: 1.2;
    text-align: center;
    color: var(--ink-soft);
  }
  .divider {
    width: 300px;
    margin-top: 22px;
    border-top: 1.5px dashed var(--ink-soft);
  }
  .title {
    margin-top: 38px;
    font-family: "Montserrat", sans-serif;
    font-weight: 600;
    font-size: 60px;
    letter-spacing: 5px;
    color: var(--ink);
  }
  .subtitle-row {
    position: relative;
    width: 330px;
    display: flex;
    align-items: center;
    gap: 14px;
    margin-top: 2px;
  }
  .subtitle-row .rule { height: 2px; width: 42px; background: var(--ink-soft); }
  .subtitle {
    font-family: "Marck Script", cursive;
    font-size: 40px;
    color: var(--ink);
  }
  .stamp {
    position: absolute;
    right: -6px; top: 8px;
    transform: rotate(-8deg);
    border: 1.5px solid var(--ink);
    padding: 4px 6px;
    font-family: "Oswald", sans-serif;
    font-weight: 500;
    font-size: 12px;
    line-height: 1.1;
    text-align: center;
    letter-spacing: .5px;
  }
  .flavour-art {
    margin-top: 40px;
    width: 300px;
    height: 150px;
    border-radius: 50% / 40%;
  }
  .flavour-art.cashew-basil {
    background: linear-gradient(90deg, var(--nut) 0%, var(--nut) 55%, var(--leaf) 100%);
    opacity: .85;
  }
  .flavour-art.goji-cocoa {
    background: linear-gradient(90deg, var(--berry) 0%, var(--berry) 50%, var(--bean) 100%);
    opacity: .85;
  }
  .flavour {
    margin-top: 34px;
    font-family: "Oswald", sans-serif;
    font-weight: 500;
    font-size: 28px;
    letter-spacing: 1.5px;
    color: var(--green);
  }
  .ribbon { margin-top: 10px; width: 340px; height: 50px; }
  .ribbon text {
    font-family: "Oswald", sans-serif;
    font-size: 20px;
    letter-spacing: 1.5px;
    fill: var(--ribbon-text);
  }
  .weight {
    margin-top: 22px;
    font-family: "Oswald", sans-serif;
    font-size: 24px;
    letter-spacing: 2px;
    color: var(--ink);
  }
</style>
</head>
<body>

  <article class="label">
    <div class="brand-mark"></div>
    <p class="brand-name">Шоколадная мастерская<br>в Заречной Слободке</p>
    <div class="divider"></div>
    <h1 class="title">ШОКОЛАД</h1>
    <div class="subtitle-row">
      <span class="rule"></span>
      <span class="subtitle">на меду</span>
      <span class="rule"></span>
      <span class="stamp">МЁД<br>ВМЕСТО<br>САХАРА</span>
    </div>
    <div class="flavour-art cashew-basil" role="img" aria-label="Иллюстрация: орехи кешью и листья базилика"></div>
    <p class="flavour">С КАРДАМОНОМ</p>
    <svg class="ribbon" viewBox="0 0 340 50" aria-label="Горький, 70% какао">
      <polygon points="0,8 30,8 30,46 0,46 12,27" fill="var(--ribbon)"/>
      <polygon points="340,8 310,8 310,46 340,46 328,27" fill="var(--ribbon)"/>
      <rect x="22" y="2" width="296" height="38" fill="var(--ribbon)"/>
      <text x="170" y="29" text-anchor="middle">ГОРЬКИЙ | 70% КАКАО</text>
    </svg>
    <p class="weight">90 ГР</p>
  </article>

  <article class="label">
    <div class="brand-mark"></div>
    <p class="brand-name">Шоколадная мастерская<br>в Заречной Слободке</p>
    <div class="divider"></div>
    <h1 class="title">ШОКОЛАД</h1>
    <div class="subtitle-row">
      <span class="rule"></span>
      <span class="subtitle">на меду</span>
      <span class="rule"></span>
      <span class="stamp">МЁД<br>ВМЕСТО<br>САХАРА</span>
    </div>
    <div class="flavour-art goji-cocoa" role="img" aria-label="Иллюстрация: ягоды годжи и дроблёные какао-бобы"></div>
    <p class="flavour">С КАРДАМОНОМ</p>
    <svg class="ribbon" viewBox="0 0 340 50" aria-label="Горький, 70% какао">
      <polygon points="0,8 30,8 30,46 0,46 12,27" fill="var(--ribbon)"/>
      <polygon points="340,8 310,8 310,46 340,46 328,27" fill="var(--ribbon)"/>
      <rect x="22" y="2" width="296" height="38" fill="var(--ribbon)"/>
      <text x="170" y="29" text-anchor="middle">ГОРЬКИЙ | 70% КАКАО</text>
    </svg>
    <p class="weight">90 ГР</p>
  </article>

</body>
</html>
```